依頼詳細
この企画実施のため、名古屋市内の全小学校に同様のデザインでポスターとチラシ配布を行うもの。
記載項目
施設名、電話番号、住所、ホームページへのリンク用QRコードを記載ください。
サイズ
A4
ページ数
片面
希望イメージ
シンプル 複雑
単色 カラフル
暗い 明るい
日常 高級
遊び心 厳粛
未来的 伝統的
女性的 男性的
希望する色
黄・オレンジ系
納品ファイル
• 高解像度JPG (.jpg)
補足説明
PDFデータもあわせて頂きます。

まずは初校提案をお願いします。
正式に依頼するとなったあと、数回文言修正のお願いをすることになります。

イベントの目的・主旨としては
ボルダリングジムPR促進、加えて、ボルダリング人口増を目的としています。
※特に、ボルダリングが「頭と身体を使う全身運動。体幹・想像力醸成に寄与」である旨PRしたく
また、“小学生”“初心者”に限定して実施することにより、その後親子での定期的な来場につなげる。

全体のバランスが良かったです

みなさま、今回応募頂きありがとうございます。
数多く応募頂き、それぞれ個性的であり、今回もかなり悩んで選択いたしました。
今後もよろしくお願いいたします。

```html
<!DOCTYPE html>
<html lang="ja">
<head>
<meta charset="utf-8">
<title>ボルダリング大会 in summer</title>
<link rel="stylesheet" href="https://fonts.googleapis.com/css2?family=M+PLUS+Rounded+1c:wght@700;800;900&family=Fredoka:wght@700&family=Noto+Sans+JP:wght@400;500;700;900&display=swap">
<style>
:root{
  --sky-top:#fdf1b0;
  --sky-mid:#fde9a0;
  --aqua:#c9f4f4;
  --aqua-deep:#b6eef0;
  --sun:#f7b733;
  --sun-light:#f9cf55;
  --orange:#f08a24;
  --coral:#f4673a;
  --ink:#2a2a2a;
  --frame:#efb94a;
  --white:#ffffff;
}
*{margin:0;padding:0;box-sizing:border-box}
html,body{width:849px;height:1200px;overflow:hidden}
body{font-family:"Noto Sans JP",sans-serif;color:var(--ink)}
.poster{position:relative;width:849px;height:1200px;overflow:hidden;
  background:linear-gradient(180deg,var(--sky-top) 0%,var(--sky-mid) 26%,var(--aqua) 38%,var(--aqua) 100%)}
.bubbles{position:absolute;inset:0;
  background:radial-gradient(circle at 22% 10%,rgba(250,205,110,.45),transparent 22%),
             radial-gradient(circle at 78% 14%,rgba(250,205,110,.4),transparent 24%),
             radial-gradient(circle at 50% 28%,rgba(250,205,110,.3),transparent 20%),
             radial-gradient(circle at 85% 60%,rgba(150,225,235,.5),transparent 16%),
             radial-gradient(circle at 12% 66%,rgba(150,225,235,.45),transparent 14%)}
.abs{position:absolute}
.eyebrow{top:72px;left:0;width:100%;text-align:center;font-family:"M PLUS Rounded 1c",sans-serif;font-weight:900;font-size:35px;color:var(--sun-light);-webkit-text-stroke:1.5px var(--sun)}
.title{top:132px;left:0;width:100%;text-align:center;font-family:"M PLUS Rounded 1c",sans-serif;font-weight:900;font-size:76px;letter-spacing:1px;color:var(--sun);-webkit-text-stroke:3px var(--orange);line-height:1}
.season{top:215px;left:0;width:100%;text-align:center;font-family:"Fredoka",sans-serif;font-weight:700;font-size:82px;letter-spacing:3px;color:var(--coral);line-height:1}
.sponsors{top:308px;left:0;width:100%;text-align:center;font-size:17px;font-weight:500;letter-spacing:1.5px}
.sponsors span{margin:0 10px}
.card{background:var(--white)}
.card .frame{position:absolute;inset:9px;border:2px solid var(--frame)}
.schedule{left:72px;top:344px;width:705px;height:261px}
.date{position:absolute;top:20px;left:0;width:100%;text-align:center;font-weight:900;font-size:29px}
.times{position:absolute;left:30px;top:83px;font-size:25px;line-height:29px}
.program{position:absolute;left:313px;top:88px;font-size:19.5px;line-height:24.5px}
.stat{top:618px;height:117px;display:flex;align-items:center;justify-content:center;font-weight:900;font-size:41px}
.capacity{left:64px;width:339px}
.fee{left:444px;width:341px;justify-content:flex-start;padding-left:40px}
.fee-notes{left:460px;top:743px;font-size:14px;font-weight:700;line-height:20px}
.heading{font-weight:900;font-size:31px;left:42px}
.rules{left:26px;top:850px;font-size:18.5px;line-height:26px}
.apply{left:26px;top:1002px;font-size:18px;line-height:26px}
.info-box{left:25px;top:1095px;width:586px;height:89px;border-radius:6px}
.qr-box{left:637px;top:987px;width:199px;height:195px;border-radius:8px}
</style>
</head>
<body>
<main class="poster">
  <div class="bubbles" role="img" aria-label="柔らかな黄色と水色の泡模様の背景"></div>

  <p class="abs eyebrow">小学生(初心者)限定！</p>
  <h1 class="abs title">ボルダリング大会</h1>
  <p class="abs season">in summer</p>
  <p class="abs sponsors"><span>主催:東陽ひかり不動産株式会社</span><span>後援:みずほ台教育委員会</span></p>

  <section class="abs card schedule">
    <div class="frame"></div>
    <p class="date">2022年8月12日(金)・8月19日(金)</p>
    <p class="times">1回目:9:00〜10:00<br>2回目:10:30〜11:30<br>3回目:13:00〜14:00<br>4回目:14:30〜15:30<br>(両日とも)</p>
    <p class="program">【1回60分】<br>☆最初の30分間スタッフによる<br>ボルダリング指導実施<br>☆その後30分間は、2組に分かれ<br>ボルダリング・playwallを体験</p>
  </section>

  <section class="abs card stat capacity"><div class="frame"></div>定員数:各12名</section>
  <section class="abs card stat fee"><div class="frame"></div>料金：800円</section>
  <p class="abs fee-notes">※税込<br>※ボルダリングシューズ、初心者指導付</p>

  <h2 class="abs heading" style="top:800px">○参加者注意事項○</h2>
  <ul class="abs rules" style="list-style:none">
    <li>・動きやすい服装(スカートNG)</li>
    <li>・当該体験会参加後にジムを利用する場合、初回登録料が必要になります。</li>
    <li>・保護者同伴必須</li>
  </ul>

  <h2 class="abs heading" style="top:952px">○申し込み方法○</h2>
  <p class="abs apply">7/16(土)10:00〜専用Web申込ページより開始<br>※あおば港スポーツ&amp;カルチャーの<br>トップページにある「体験教室・イベント申込」</p>

  <div class="abs card info-box"></div>
  <div class="abs card qr-box"></div>
</main>
</body>
</html>
```